Tolvane Air and Electrical Website

Simple and easy to use website for a Electrical and Air Conditioning contracting business.Use stock photosOnline contact portallogo still to be supplied

Target Market(s)

Mums and Dads who want a local contractor

Coding

Coded - Design and coding required

Number of Pages Required

2 page

Font styles to use
Sans Serif

Colors
f04a50
3276b5
33a6d7

Requirements
Must have
• Simple and easy to use
• Ph number
• 4 web address; linked to page
• 0417385926
• tolvane.com.au
• tolvaneelectrical.com.au
• tolvaneairandelectrical.com.au
• tolvaneair.com.au
Nice to have
• Split System Air Con Picture
• Electrical Pictures

```html
<!DOCTYPE html>
<html lang="en">
<head>
<meta charset="utf-8">
<title>Tolvane Air and Electrical</title>
<link href="https://fonts.googleapis.com/css2?family=Arimo:ital,wght@0,400;0,700;1,400&display=swap" rel="stylesheet">
<style>
:root{
  --red:#f04a50;
  --blue:#3276b5;
  --sky:#33a6d7;
  --ink:#1f1f1f;
  --dark:#252525;
  --white:#ffffff;
  --muted:#cfcfcf;
}
*{box-sizing:border-box;margin:0;padding:0}
html,body{width:1200px;height:2549px;overflow:hidden;background:var(--white)}
body{position:relative;font-family:"Arimo",Arial,sans-serif;color:var(--ink)}
a{color:inherit;text-decoration:none}

.hero{position:absolute;left:0;top:0;width:1200px;height:674px;
  background:linear-gradient(120deg,#8a8a8a 0%,#b9b9b9 35%,#d2d2d2 60%,#9a9a9a 100%)}
.hero-photo{position:absolute;inset:0;background:radial-gradient(ellipse at 25% 35%,rgba(214,110,50,.35),transparent 30%),linear-gradient(rgba(40,40,40,.35),rgba(40,40,40,.45))}
.topbar{position:absolute;left:0;top:0;width:1200px;height:62px;background:rgba(35,35,35,.85)}
.brand{position:absolute;left:88px;top:17px;display:flex;align-items:center;gap:10px;color:var(--white);font-size:20px;font-weight:700}
.brand-dot{width:22px;height:22px;background:var(--red)}
.nav{position:absolute;left:722px;top:20px;display:flex;gap:42px;color:var(--white);font-size:17px}
.nav a.active{position:relative}
.nav a.active::after{content:"";position:absolute;left:0;bottom:-8px;width:15px;height:2px;background:var(--red)}
.phone{position:absolute;right:88px;top:19px;display:flex;align-items:center;gap:10px;color:var(--white);font-size:17px}
.phone-icon{width:20px;height:20px;background:var(--red);border-radius:3px;display:flex;align-items:center;justify-content:center}

.domains{position:absolute;left:902px;top:106px;width:210px;display:flex;flex-direction:column;gap:11px}
.domain{height:28px;background:rgba(35,35,35,.85);border-radius:4px;color:var(--white);font-size:12px;display:flex;align-items:center;justify-content:space-between;padding:0 10px 0 12px}

.tagline{position:absolute;left:0;top:530px;width:1200px;text-align:center;color:var(--white);font-size:28px;letter-spacing:12px}
.cta{position:absolute;left:478px;top:587px;width:243px;height:40px;background:var(--red);border-radius:4px;color:var(--white);font-size:17px;letter-spacing:1px;display:flex;align-items:center;justify-content:center}

.feature{position:absolute;left:174px;width:852px}
.feature h2{font-size:37px;font-weight:400;font-style:italic;color:var(--blue);line-height:1}
.feature h2::after{content:"";display:block;width:76px;height:3px;background:var(--red);margin-top:10px}
.feature .copy{position:absolute;left:0;width:505px;font-size:16px;line-height:22px;color:var(--ink)}
.feature .copy p+p{margin-top:22px}
.shot{position:absolute;left:517px;width:335px;height:223px}
.shot::before{content:"";position:absolute;left:10px;top:16px;width:335px;height:223px;background:var(--red)}
.shot .fill{position:absolute;inset:0}

.footer{position:absolute;left:0;top:2309px;width:1200px;height:240px;background:var(--dark);color:var(--muted)}
.footer-badge{position:absolute;left:558px;top:2275px;width:84px;height:84px;border-radius:50%;background:var(--dark);border:3px solid var(--white)}
.visit{position:absolute;left:174px;top:84px;font-size:13px;letter-spacing:1px}
.visit h3{font-size:13px;font-weight:400;margin-bottom:13px}
.visit a{display:block;font-size:10px;margin-left:18px;line-height:21px;letter-spacing:1px}
.contact{position:absolute;left:691px;top:83px;font-size:12px;letter-spacing:1px}
.contact h3{font-size:13px;font-weight:400;margin-bottom:12px}
.contact p{font-size:10px;line-height:24px;display:flex;align-items:center;gap:9px}
.map{position:absolute;left:863px;top:62px;width:163px;height:115px;background:linear-gradient(135deg,#e6e2d8,#d8e5cf 50%,#e4e0ea)}
.copyright{position:absolute;left:0;top:218px;width:1200px;text-align:center;font-size:10px;letter-spacing:5px}
</style>
</head>
<body>

<header class="hero">
  <div class="hero-photo" role="img" aria-label="Electrician in a hard hat fitting a ceiling light"></div>
  <div class="topbar">
    <div class="brand"><span class="brand-dot"></span>Tolvane Air and Electrical</div>
    <nav class="nav"><a class="active" href="#">Home</a><a href="#">Services</a></nav>
    <a class="phone" href="tel:0417385926"><span class="phone-icon"><svg width="12" height="12" viewBox="0 0 24 24"><path fill="#fff" d="M6.6 10.8c1.4 2.8 3.8 5.1 6.6 6.6l2.2-2.2c.3-.3.7-.4 1-.2 1.1.4 2.3.6 3.6.6.6 0 1 .4 1 1V20c0 .6-.4 1-1 1C10.6 21 3 13.4 3 4c0-.6.4-1 1-1h3.5c.6 0 1 .4 1 1 0 1.3.2 2.5.6 3.6.1.3 0 .7-.2 1z"/></svg></span>0417385926</a>
  </div>
  <div class="domains">
    <a class="domain" href="#">tolvane.com.au<svg width="10" height="14" viewBox="0 0 10 14"><path d="M2 1l6 6-6 6" stroke="#f04a50" stroke-width="2.2" fill="none"/></svg></a>
    <a class="domain" href="#">tolvaneelectrical.com.au<svg width="10" height="14" viewBox="0 0 10 14"><path d="M2 1l6 6-6 6" stroke="#f04a50" stroke-width="2.2" fill="none"/></svg></a>
    <a class="domain" href="#">tolvaneairandelectrical.com.au<svg width="10" height="14" viewBox="0 0 10 14"><path d="M2 1l6 6-6 6" stroke="#f04a50" stroke-width="2.2" fill="none"/></svg></a>
    <a class="domain" href="#">tolvaneair.com.au<svg width="10" height="14" viewBox="0 0 10 14"><path d="M2 1l6 6-6 6" stroke="#f04a50" stroke-width="2.2" fill="none"/></svg></a>
  </div>
  <p class="tagline">A superior level of knowledge</p>
  <a class="cta" href="#">Our Services</a>
</header>

<section class="feature" style="top:770px">
  <h2>ABOUT</h2>
  <div class="copy" style="top:85px">
    <p>With over 17 years' experience in the Electrical Industry, Tolvane Electrical provides a superior level of knowledge, a broad range of products and a high standard of customer service.</p>
    <p>To provide our customers with an immediate response within their timeframe, and deliver on-time, every time. Our friendly tradesmen are always professionally attired and treat your home or business with respect - we leave our jobs clean and tidy.</p>
  </div>
  <div class="shot" style="top:44px"><div class="fill" role="img" aria-label="Technician servicing a split system air conditioner" style="background:linear-gradient(120deg,#d9d6cf,#eeeeec 55%,#c9c6bd)"></div></div>
</section>

<section class="feature" style="top:1155px">
  <h2>WHY US?</h2>
  <div class="copy" style="top:85px">
    <p>On Time We arrive on time. If there is an unavoidable delay we’ll call ahead to let you know when we’ll be there. We also respond to your phone calls and emails within 24 hours.</p>
  </div>
  <div class="shot" style="top:44px"><div class="fill" role="img" aria-label="Electrician in overalls holding a coil of cable" style="background:linear-gradient(180deg,#e3e6ea,#dfe2e6 50%,#c9ced6)"></div></div>
</section>

<section class="feature" style="top:1507px">
  <h2>Quality</h2>
  <div class="copy" style="top:85px">
    <p>We are committed to best practice electrical safety standards and highest quality performance on the job.</p>
    <p>Our team of qualified and apprentice electricians provide personalised service based on professionalism and integrity.</p>
    <p>We aim to build long term business relationships and offer information and advice when you need it.</p>
  </div>
  <div class="shot" style="top:44px"><div class="fill" role="img" aria-label="Hands wiring a wall power point" style="background:linear-gradient(110deg,#6f7478,#b8bcbf 45%,#e2e6e6)"></div></div>
</section>

<section class="feature" style="top:1903px">
  <h2>Price</h2>
  <div class="copy" style="top:85px">
    <p>Price is always important and our standard rates are competitive. Where jobs require an individual approach, we provide a comprehensive quote. Work is completed according to the quote at the agreed price.</p>
    <p>Registered Contractor Tolvane Electrical is a registered electrical contractor with Energy Safety Authority, and also a registered RRC contractor to install and decomission split system air conditioning</p>
  </div>
  <div class="shot" style="top:44px"><div class="fill" role="img" aria-label="Technician fitting a ceiling cassette air conditioner" style="background:linear-gradient(120deg,#eef6fb,#d9eaf5 55%,#f4f8fb)"></div></div>
</section>

<footer class="footer">
  <div class="visit">
    <h3>Visit Us</h3>
    <a href="#">tolvane.com.au</a>
    <a href="#">tolvaneelectrical.com.au</a>
    <a href="#">tolvaneairandelectrical.com.au</a>
    <a href="#">tolvaneair.com.au</a>
  </div>
  <div class="contact">
    <h3>Declan Tolvane</h3>
    <p><svg width="9" height="9" viewBox="0 0 24 24"><path fill="#33a6d7" d="M6.6 10.8c1.4 2.8 3.8 5.1 6.6 6.6l2.2-2.2c.3-.3.7-.4 1-.2 1.1.4 2.3.6 3.6.6.6 0 1 .4 1 1V20c0 .6-.4 1-1 1C10.6 21 3 13.4 3 4c0-.6.4-1 1-1h3.5c.6 0 1 .4 1 1 0 1.3.2 2.5.6 3.6.1.3 0 .7-.2 1z"/></svg>0417385926</p>
    <p><svg width="9" height="11" viewBox="0 0 18 24"><path fill="#33a6d7" d="M9 0C4 0 0 4 0 9c0 7 9 15 9 15s9-8 9-15c0-5-4-9-9-9zm0 12a3 3 0 110-6 3 3 0 010 6z"/></svg>Ashvale VIC 3170</p>
  </div>
  <div class="map" role="img" aria-label="Street map of the service area"></div>
  <p class="copyright">Copyrights 2019</p>
</footer>
<div class="footer-badge"></div>

</body>
</html>
```